Meridale Hair Studio Needs a new appointment business card

We need a new appointment card for our hair salon.

I Dont want bright out there colours.
I would like it to be neat, clean, easy to read. White, Black, with a hint of colour if needed.

We need
-Logo
-Phone number 47260385
-Mobile Number: 0417360528
Address: Shop 3/217 Tarrow Street, Kelby Court, Dunmore 4812

BACK SIDE OF CARD
- Appointment Time & Date (White background so we are able to write on it)
(If you are unable to make your appointment please contact us ASAP 47260385)

I also would like the chatterly and Snapfold logo(Find us on Chatterly)(find us on Snapfold)

Target Market(s)

appointment card simple to read. all information for their next appoint For all our clients male and female

Industry/Entity Type

Hairdresser

Contact Information for Business Card

-Logo
-Phone number 47260385

BACK SIDE OF CARD

Font styles to use
Serif
Sans Serif
Script

Requirements
Must have
• White Back ground on backside with appointment deatils so we are able to write information (like appointment time and date)
Nice to have
• Find us on Chatterly
and
snapfold - meridale_hairstudio
Should not have
• BRIGHT COLOURS

```html
<!DOCTYPE html>
<html lang="en">
<head>
<meta charset="utf-8">
<title>Meridale Hair Studio – Appointment Card</title>
<link rel="stylesheet" href="https://fonts.googleapis.com/css2?family=Cinzel:wght@500&family=Tinos&family=Arimo&display=swap">
<style>
  :root {
    --stage: #d4d5d8;
    --card-dark: #1f1f20;
    --card-light: #ffffff;
    --logo-grey: #8e8e90;
    --ink-light: #ffffff;
    --ink-dark: #2b2b2b;
    --rule-dark: #cfcfcf;
    --rule-light: #3a3a3a;
    --social-dot: #6d6d70;
  }
  * { margin: 0; padding: 0; box-sizing: border-box; }
  html, body {
    width: 1200px; height: 1200px; overflow: hidden;
    background: var(--stage);
  }
  .stage { position: relative; width: 1200px; height: 1200px; }
  .card {
    position: absolute; left: 280px; width: 640px; height: 390px;
    border-radius: 24px;
  }
  .card-front { top: 150px; background: var(--card-dark); color: var(--ink-light); }
  .card-back  { top: 650px; background: var(--card-light); color: var(--ink-dark); }

  /* Front */
  .brand { position: absolute; left: 0; right: 0; top: 112px; text-align: center; }
  .brand-name {
    font-family: "Cinzel", serif; font-weight: 500;
    font-size: 58px; letter-spacing: 2px; color: var(--logo-grey);
    line-height: 1;
  }
  .brand-sub {
    font-family: "Arimo", sans-serif; font-size: 17px; letter-spacing: 1px;
    color: var(--ink-light); margin-top: 8px;
  }
  .rule { position: absolute; left: 110px; right: 60px; height: 1px; background: var(--rule-dark); }
  .rule-top { top: 250px; }
  .rule-bottom { top: 352px; left: 80px; right: 110px; }
  .address {
    position: absolute; left: 0; right: 0; top: 272px;
    text-align: center; font-family: "Tinos", serif; font-size: 17px;
  }
  .contacts {
    position: absolute; left: 0; right: 0; top: 308px;
    display: flex; justify-content: center; align-items: center;
    font-family: "Arimo", sans-serif; font-size: 16px;
  }
  .contact { display: flex; align-items: center; gap: 6px; padding: 0 10px; }
  .divider { width: 1px; height: 34px; background: var(--rule-dark); }
  .icon { fill: var(--ink-light); display: block; }
  .address .icon { display: inline-block; vertical-align: -3px; margin-right: 12px; }

  /* Back */
  .appt-title {
    position: absolute; left: 0; right: 0; top: 58px; text-align: center;
    font-family: "Tinos", serif; font-size: 22px; font-weight: normal; letter-spacing: 1px;
  }
  .field {
    position: absolute; left: 150px; display: flex; align-items: flex-end;
    font-family: "Tinos", serif; font-size: 16px;
  }
  .field-date { top: 125px; }
  .field-time { top: 180px; }
  .field-label { width: 70px; }
  .field-line { width: 160px; height: 1px; background: var(--rule-light); margin-left: 10px; margin-bottom: 3px; }
  .ampm { font-family: "Arimo", sans-serif; font-size: 11px; margin-left: 20px; }
  .socials {
    position: absolute; left: 0; right: 0; top: 268px;
    display: flex; justify-content: center; gap: 48px;
    font-family: "Tinos", serif; font-size: 16px;
  }
  .social { display: flex; align-items: center; gap: 8px; }
  .social-dot { width: 26px; height: 26px; border-radius: 50%; background: var(--social-dot); }
</style>
</head>
<body>
<main class="stage">
  <section class="card card-front" aria-label="Front of card">
    <div class="brand">
      <div class="brand-name">MERIDALE</div>
      <div class="brand-sub">HAIR-STUDIO</div>
    </div>
    <div class="rule rule-top"></div>
    <p class="address">
      <svg class="icon" width="12" height="16" viewBox="0 0 12 16" aria-hidden="true"><path d="M6 0a5 5 0 0 0-5 5c0 3.5 5 8 5 8s5-4.5 5-8a5 5 0 0 0-5-5zm0 7a2 2 0 1 1 0-4 2 2 0 0 1 0 4z"/><rect x="1" y="14" width="10" height="2" rx="1"/></svg>Shop 3/217 Tarrow Street, Kelby Court, Dunmore 4812
    </p>
    <div class="contacts">
      <div class="contact">
        <span>47260385</span>
        <svg class="icon" width="14" height="14" viewBox="0 0 24 24" aria-hidden="true"><path d="M6.6 10.8a15.1 15.1 0 0 0 6.6 6.6l2.2-2.2a1 1 0 0 1 1-.25 11.4 11.4 0 0 0 3.6.57 1 1 0 0 1 1 1V20a1 1 0 0 1-1 1A17 17 0 0 1 3 4a1 1 0 0 1 1-1h3.5a1 1 0 0 1 1 1c0 1.25.2 2.45.57 3.57a1 1 0 0 1-.25 1z"/></svg>
      </div>
      <div class="divider"></div>
      <div class="contact">
        <svg class="icon" width="12" height="20" viewBox="0 0 12 20" aria-hidden="true"><path d="M2 0h8a2 2 0 0 1 2 2v16a2 2 0 0 1-2 2H2a2 2 0 0 1-2-2V2a2 2 0 0 1 2-2zm0 2v14h8V2z"/></svg>
        <span>0417360528</span>
      </div>
    </div>
    <div class="rule rule-bottom"></div>
  </section>

  <section class="card card-back" aria-label="Back of card">
    <h2 class="appt-title">YOUR NEXT APPOINTMENT IS</h2>
    <div class="field field-date"><span class="field-label">DATE:</span><span class="field-line"></span></div>
    <div class="field field-time"><span class="field-label">TIME:</span><span class="field-line"></span><span class="ampm">AM / PM</span></div>
    <div class="socials">
      <div class="social"><span class="social-dot"></span><span>Chatterly</span></div>
      <div class="social"><span class="social-dot"></span><span>Snapfold</span></div>
    </div>
  </section>
</main>
</body>
</html>
```